Tutoring Site Hero Image Design

Updated Hero Concept for BrightlaneLessons.com

Create a hero that communicates “high quality, in-person private tutoring for all ages,” with warmth, credibility, and a real-life feel. The hero should move away from generic stock photography and better reflect the moments that make our service different: tutors meeting students where they are, one-on-one engagement, and a range of ages.

What the New Hero Should Convey
1. In-person, private, one-on-one support
This is the core differentiator, so the visual should feel intimate, focused, and real. Avoid anything that resembles online learning settings or learning-center classrooms.

2. Coverage of age ranges without clutter
We serve elementary through college. We do not need multiple students in the hero, but the chosen student should not skew strongly to one age group. Aim for a middle-ground age that feels inclusive, for example a middle schooler or early high schooler.

3. Realistic, authentic moments
Use photography that feels candid and warm. Natural light, home settings, kitchen tables, quiet study nooks, or library corners work well. Avoid staged stock looks, harsh lighting, or exaggerated classroom setups.

Design the hero at 2400 × 1200 px, with the focal point on the right side, safe area leaving room on the left for a stacked headline and form.

Images that I've shared as just thought starters and do not need to be used in the design.

Font styles to use
Sans Serif

Colors
0054AA
0677BA
7BADD7
CADEEF
E8F1F8
EB3D1F
EC4F4E
F09395
F8D3D4
FCEDEE
6B429C
8869AF
B7A5CE
E3DAEB
F3F0F8

```html
<!DOCTYPE html>
<html lang="en">
<head>
<meta charset="UTF-8">
<title>BrightlaneLessons.com – Hero</title>
<link rel="stylesheet" href="https://fonts.googleapis.com/css2?family=Roboto+Condensed:wght@700&family=Montserrat:wght@400;500&family=Roboto:wght@400&display=swap">
<style>
  :root {
    --blue-deep: #0054AA;
    --blue-mid: #0677BA;
    --purple: #6B429C;
    --purple-soft: #8869AF;
    --red: #EB3D1F;
    --red-soft: #EC4F4E;
    --white: #FFFFFF;
    --ink: #111111;
    --photo-warm: #E3C9A6;
    --photo-light: #F6E9D6;
    --photo-wood: #A87A52;
    --photo-teal: #1E7C86;
    --photo-blue: #1F4FA0;
  }
  * { margin: 0; padding: 0; box-sizing: border-box; }
  html, body {
    width: 1200px;
    height: 627px;
    overflow: hidden;
    background: var(--white);
  }
  .hero {
    position: relative;
    width: 1200px;
    height: 627px;
    overflow: hidden;
    background: linear-gradient(58deg, #F2401C 8%, #C93E4E 24%, var(--purple) 44%, #3A47A8 62%, var(--blue-deep) 82%);
  }
  .hero__art {
    position: absolute;
    inset: 0;
    width: 1200px;
    height: 627px;
  }
  .hero__content {
    position: absolute;
    left: 77px;
    top: 160px;
    width: 470px;
    color: var(--white);
  }
  .hero__headline {
    font-family: "Roboto Condensed", "Arial Narrow", sans-serif;
    font-weight: 700;
    font-size: 40px;
    line-height: 48px;
    letter-spacing: -0.2px;
  }
  .hero__lede {
    margin-top: 14px;
    font-family: "Montserrat", Arial, sans-serif;
    font-weight: 500;
    font-size: 17px;
    line-height: 23px;
    width: 430px;
  }
  .hero__actions {
    margin-top: 28px;
    display: flex;
    align-items: center;
    gap: 28px;
  }
  .btn-start {
    display: inline-flex;
    align-items: center;
    justify-content: center;
    width: 133px;
    height: 36px;
    background: var(--white);
    border: 1.5px solid var(--red);
    border-radius: 5px;
    color: var(--red);
    font-family: "Roboto Condensed", "Arial Narrow", sans-serif;
    font-weight: 700;
    font-size: 20px;
    text-decoration: none;
  }
  .call-line {
    display: inline-flex;
    align-items: center;
    height: 36px;
    padding: 0 12px 0 12px;
    background: linear-gradient(90deg, rgba(255,255,255,0) 0%, rgba(255,255,255,0.9) 14%, #FFFFFF 40%, #FFFFFF 88%, rgba(255,255,255,0) 100%);
    color: var(--ink);
    font-family: "Roboto", Arial, sans-serif;
    font-size: 20px;
    text-decoration: none;
  }
</style>
</head>
<body>
  <section class="hero">
    <svg class="hero__art" viewBox="0 0 1200 627" xmlns="http://www.w3.org/2000/svg">
      <defs>
        <linearGradient id="photoTone" x1="0" y1="0" x2="1" y2="1">
          <stop offset="0" stop-color="var(--photo-wood)"/>
          <stop offset="0.3" stop-color="var(--photo-warm)"/>
          <stop offset="0.55" stop-color="var(--photo-blue)"/>
          <stop offset="0.8" stop-color="var(--photo-teal)"/>
          <stop offset="1" stop-color="var(--photo-light)"/>
        </linearGradient>
        <linearGradient id="bandRed" x1="0" y1="0" x2="0" y2="1">
          <stop offset="0" stop-color="var(--red)"/>
          <stop offset="1" stop-color="var(--red-soft)"/>
        </linearGradient>
        <linearGradient id="bandPurple" x1="0" y1="0" x2="0" y2="1">
          <stop offset="0" stop-color="var(--blue-deep)"/>
          <stop offset="0.5" stop-color="var(--purple)"/>
          <stop offset="1" stop-color="var(--purple-soft)"/>
        </linearGradient>
      </defs>
      <path class="band band--red" d="M752 0 C 590 110, 545 470, 778 627 L1200 627 L1200 0 Z" fill="url(#bandRed)"/>
      <path class="band band--blue" d="M758 0 C 610 115, 575 470, 792 627 L1200 627 L1200 0 Z" fill="url(#bandPurple)"/>
      <path class="band band--accent" d="M764 0 C 625 118, 592 470, 806 627 L1200 627 L1200 0 Z" fill="var(--red)"/>
      <path class="band band--inner" d="M770 0 C 640 122, 612 470, 820 627 L1200 627 L1200 0 Z" fill="var(--purple)"/>
      <path class="hero__photo" role="img" aria-label="Photo: a tutor and a teenage student working together over notebooks at a sunlit home table" d="M776 0 C 655 126, 630 470, 834 627 L1200 627 L1200 0 Z" fill="url(#photoTone)"/>
    </svg>

    <div class="hero__content">
      <h1 class="hero__headline">One-on-one<br>support for every grade<br>from elementary to college.</h1>
      <p class="hero__lede">Connecting students with experienced, one-on-one tutors for personalized support from elementary to college.</p>
      <div class="hero__actions">
        <a class="btn-start" href="#">Get Started</a>
        <a class="call-line" href="#">Call (555) 214-8830</a>
      </div>
    </div>
  </section>
</body>
</html>
```